LUMINARA VENTURES NAMECARD

Need to design a name card with an existing logo.

As we are professional corporate services provider our name card has to project a professional image.
Should be corporate, simple & professional.

Our corporate color is maroon red but not too dull.

Please refer to our website at www.luminaraventures.com.sg

Would attach our logo herewith.

Front surface of namecard details:
LUMINARA VENTURES PTE LTD
Registration No. 208711845K

Tan Wei Ling CA (Singapore)
Director

Tel +65 6481 2957
Mobile +65 9172 3086
tan@luminaraventures.com.sg
www.luminaraventures.com.sg

47 Plover Lane
#07-12 Harbourlight Plaza
Singapore 276351

Back of namecard:-
OUR CORE SERVICES
Incorporation services
Corporate Secretarial Services
Accountancy service
Goods & Services Taxation
Corporate & Personal Taxation
Financial Reporting
Payroll Administration

AFFILIATES:
BRIGHTWAVE CORPORATE SERVICES PTE LTD
PINNACLEFORMATIONSPTE LTD
LIM MANAGEMENT SERVICES PTE LTD
RW HO AND COMPANY PTE LTD
LEDGERLY ACADEMY

```html
<!DOCTYPE html>
<html lang="en">
<head>
<meta charset="utf-8">
<title>Luminara Ventures Stationery</title>
<link href="https://fonts.googleapis.com/css2?family=Tinos:wght@400;700&family=Open+Sans:wght@400;600&display=swap" rel="stylesheet">
<style>
  :root {
    --brand-red: #cf1a2e;
    --paper: #ffffff;
    --backdrop: #c2c2c2;
    --ink: #3a3a3a;
    --soft-window: #ededed;
  }
  * { box-sizing: border-box; margin: 0; padding: 0; }
  html, body { width: 1200px; height: 1200px; overflow: hidden; }
  body {
    background: var(--backdrop);
    position: relative;
    font-family: "Tinos", "Times New Roman", serif;
  }
  .icon-defs { position: absolute; width: 0; height: 0; }

  .wordmark {
    font-family: "Tinos", "Times New Roman", serif;
    font-weight: 700;
    text-transform: uppercase;
    line-height: 0.92;
    letter-spacing: -0.01em;
  }

  /* Letterhead */
  .letterhead {
    position: absolute; left: 164px; top: 344px;
    width: 399px; height: 521px;
    background: var(--paper);
  }
  .letterhead-header {
    height: 66px; background: var(--brand-red); color: var(--paper);
    position: relative;
  }
  .letterhead-header .wordmark {
    position: absolute; left: 19px; top: 13px; font-size: 21px;
  }
  .letterhead-header .reg-no {
    position: absolute; left: 19px; top: 55px;
    font-size: 4px; letter-spacing: 0.12em;
  }
  .letterhead-header .contact {
    position: absolute; left: 300px; top: 6px;
    font-size: 6.4px; line-height: 7.4px;
  }
  .letter-body {
    position: absolute; left: 22px; top: 154px; width: 360px;
    font-family: "Open Sans", Arial, sans-serif;
    font-size: 7.6px; line-height: 12px; color: var(--ink);
  }
  .letter-body p { margin-bottom: 12px; }
  .letterhead-footer {
    position: absolute; left: 0; right: 0; bottom: 0; height: 17px;
    background: var(--brand-red);
  }

  /* Name card (back + front side by side) */
  .namecard {
    position: absolute; left: 734px; top: 319px;
    width: 248px; height: 141px; display: flex;
  }
  .card-back {
    width: 124px; height: 100%; background: var(--brand-red);
    color: var(--paper); padding: 22px 10px 0 10px;
  }
  .card-back h3 { font-size: 5.4px; font-weight: 700; margin-bottom: 2px; }
  .card-back ul { list-style: none; font-size: 3.8px; line-height: 5px; margin-bottom: 5px; }
  .card-back .affiliates li { font-weight: 700; font-size: 3.7px; line-height: 4.6px; }
  .card-back .company { font-size: 4.2px; font-weight: 700; margin-top: 3px; }
  .card-back .reg-no { font-size: 3.8px; font-weight: 700; margin-top: 5px; }
  .card-front {
    width: 124px; height: 100%; background: var(--paper);
    color: var(--brand-red); padding: 19px 0 0 22px;
  }
  .card-front .wordmark { font-size: 14.5px; }
  .card-front .person-name { font-size: 10.5px; margin-top: 7px; line-height: 11px; }
  .card-front .role { font-size: 7px; line-height: 8px; }
  .contact-list { list-style: none; }
  .contact-list li { display: flex; align-items: flex-start; }
  .contact-list svg { fill: var(--brand-red); flex: none; }
  .card-front .contact-list { font-size: 5px; line-height: 5.6px; margin-top: 1px; }
  .card-front .contact-list svg { width: 5px; height: 5px; margin-right: 3px; }
  .card-front .indent { padding-left: 8px; }

  /* Envelope back */
  .envelope-back {
    position: absolute; left: 662px; top: 503px;
    width: 377px; height: 177px; background: var(--paper);
  }
  .envelope-flap { position: absolute; left: 0; top: 0; }
  .envelope-back .wordmark {
    position: absolute; left: 0; right: 0; top: 10px;
    text-align: center; color: var(--paper); font-size: 9.5px;
  }

  /* Envelope front */
  .envelope-front {
    position: absolute; left: 662px; top: 696px;
    width: 377px; height: 176px; background: var(--paper);
    color: var(--brand-red);
  }
  .envelope-front .contact-list {
    position: absolute; left: 22px; top: 15px;
    font-size: 8.3px; line-height: 9.3px;
  }
  .envelope-front .contact-list svg { width: 7px; height: 7px; margin: 1px 4px 0 0; }
  .envelope-front .indent { padding-left: 11px; }
  .envelope-front .wordmark {
    position: absolute; right: 22px; top: 17px; font-size: 22px; text-align: left;
  }
  .address-window {
    position: absolute; left: 240px; top: 112px; width: 101px; height: 40px;
    background: var(--soft-window); border-radius: 6px;
  }
  .envelope-band {
    position: absolute; left: 0; right: 0; bottom: 0; height: 13px;
    background: var(--brand-red);
  }
</style>
</head>
<body>

<svg class="icon-defs" aria-hidden="true">
  <symbol id="icon-pin" viewBox="0 0 10 10"><path d="M5 0a3.5 3.5 0 0 0-3.5 3.5C1.5 6 5 10 5 10s3.5-4 3.5-6.5A3.5 3.5 0 0 0 5 0zm0 5a1.4 1.4 0 1 1 0-2.8A1.4 1.4 0 0 1 5 5z"/></symbol>
  <symbol id="icon-phone" viewBox="0 0 10 10"><path d="M2 0.5l2 2.2-1 1.2a6 6 0 0 0 3.1 3.1l1.2-1 2.2 2-1.2 1.5C4.5 9.6 0.4 5.5 0.5 1.7z"/></symbol>
  <symbol id="icon-mobile" viewBox="0 0 10 10"><path d="M2.5 0h5v10h-5zM3.3 1v6.6h3.4V1zM4.5 8.2h1v1h-1z"/></symbol>
  <symbol id="icon-mail" viewBox="0 0 10 10"><path d="M0 2h10v6H0zm1 1v.3l4 2.4 4-2.4V3zm0 1.5V7h8V4.5L5 6.8z"/></symbol>
  <symbol id="icon-globe" viewBox="0 0 10 10"><path d="M5 0a5 5 0 1 0 0 10A5 5 0 0 0 5 0zm0 1c.7.6 1.2 1.8 1.4 3.5H3.6C3.8 2.8 4.3 1.6 5 1zM1.1 5.5h1.5c.1 1.3.4 2.4.9 3.1A4 4 0 0 1 1.1 5.5zm0-1A4 4 0 0 1 3.5 1.4c-.5.8-.8 1.9-.9 3.1zm2.5 1h2.8C6.2 7.2 5.7 8.4 5 9 4.3 8.4 3.8 7.2 3.6 5.5zm2.9 3.1c.5-.7.8-1.8.9-3.1h1.5a4 4 0 0 1-2.4 3.1zm.9-4.1c-.1-1.2-.4-2.3-.9-3.1a4 4 0 0 1 2.4 3.1z"/></symbol>
</svg>

<section class="letterhead">
  <header class="letterhead-header">
    <div class="wordmark">Luminara<br>Ventures</div>
    <div class="reg-no">Registration No. 208711845K</div>
    <address class="contact" style="font-style:normal">
      47 Plover Lane<br>#07-12 Harbourlight Plaza<br>Singapore 276351<br>
      +65 6481 2957<br>+65 9172 3086<br>tan@luminaraventures.com.sg<br>www.luminaraventures.com.sg
    </address>
  </header>
  <div class="letter-body">
    <p>Dear [Recipient],</p>
    <p>We love the look of this stationery just the way it is. But you can add your own personal touch in almost no time.</p>
    <p>On the Design tab of the ribbon, check out the Themes, Colors, and Fonts galleries to preview different looks from a variety of choices. Then just click to apply the one you like.</p>
    <p>We’ve also created styles that let you match the formatting you see in this letter with just a click. On the Home tab of the ribbon, check out the Styles gallery for all styles used in this letter.</p>
    <p>Ready to add your digits? No problem. Just double-click the header area to add your contact information.</p>
    <p style="margin-bottom:0">Warm regards,<br>Arlen</p>
  </div>
  <div class="letterhead-footer"></div>
</section>

<section class="namecard">
  <div class="card-back">
    <h3>OUR CORE SERVICES</h3>
    <ul>
      <li>Incorporation services</li>
      <li>Corporate Secretarial Services</li>
      <li>Accountancy service</li>
      <li>Goods &amp; Services Taxation</li>
      <li>Corporate &amp; Personal Taxation</li>
      <li>Financial Reporting</li>
      <li>Payroll Administration</li>
    </ul>
    <h3>AFFILIATES:</h3>
    <ul class="affiliates">
      <li>BRIGHTWAVE CORPORATE SERVICES PTE LTD</li>
      <li>PINNACLEFORMATIONSPTE LTD</li>
      <li>LIM MANAGEMENT SERVICES PTE LTD</li>
      <li>RW HO AND COMPANY PTE LTD</li>
      <li>LEDGERLY ACADEMY</li>
    </ul>
    <div class="company">LUMINARA VENTURES PTE LTD</div>
    <div class="reg-no">Registration No. 208711845K</div>
  </div>
  <div class="card-front">
    <div class="wordmark">Luminara<br>Ventures</div>
    <div class="person-name">Tan Wei Ling CA</div>
    <div class="role">Director</div>
    <ul class="contact-list">
      <li><svg><use href="#icon-pin"/></svg>47 Plover Lane</li>
      <li class="indent">#07-12 Harbourlight Plaza</li>
      <li class="indent">Singapore 276351</li>
      <li><svg><use href="#icon-phone"/></svg>+65 6481 2957</li>
      <li><svg><use href="#icon-mobile"/></svg>+65 9172 3086</li>
      <li><svg><use href="#icon-mail"/></svg>tan@luminaraventures.com.sg</li>
      <li><svg><use href="#icon-globe"/></svg>www.luminaraventures.com.sg</li>
    </ul>
  </div>
</section>

<section class="envelope-back">
  <svg class="envelope-flap" width="377" height="36" viewBox="0 0 377 36" aria-hidden="true">
    <polygon points="0,0 377,0 355,36 22,36" fill="var(--brand-red)"/>
  </svg>
  <div class="wordmark">Luminara<br>Ventures</div>
</section>

<section class="envelope-front">
  <ul class="contact-list">
    <li><svg><use href="#icon-pin"/></svg>47 Plover Lane</li>
    <li class="indent">#07-12 Harbourlight Plaza</li>
    <li class="indent">Singapore 276351</li>
    <li><svg><use href="#icon-phone"/></svg>+65 6481 2957</li>
    <li><svg><use href="#icon-mobile"/></svg>+65 9172 3086</li>
    <li><svg><use href="#icon-mail"/></svg>tan@luminaraventures.com.sg</li>
    <li><svg><use href="#icon-globe"/></svg>www.luminaraventures.com.sg</li>
  </ul>
  <div class="wordmark">Luminara<br>Ventures</div>
  <div class="address-window"></div>
  <div class="envelope-band"></div>
</section>

</body>
</html>
```